Harbor of Separation Website Design

The primary objectives of this website is lead generation, create authority and enhance trust factor so that potential clients utilize Harbor of Separation services.

In an effort to provide prospects with a comprehensive explanation of the company’s services, Harbor of Separation will be creating a new website to provide, a user-friendly experience that will lead a person onto the right pathway where they will find tailored information depending on the stage they are in: Thinking of Divorce, Ready to Move Forward, and Recently Divorced.

Visitors will land on the homepage, which will give them the opportunity to select from the three types of personas shown. Messaging will be written specifically for each persona type, a lead-gen form will be present throughout the entire site, and a free downloadable form will be provided to them.

Once the lead gen form is submitted, information will be sent to Harbor of Separation consultant, who will follow up with the prospect.

Social Integration with website continue to prove Harbor of Separation authority and expertise.

Target Market(s)

Individuals who are considering or our in the process of divorce find themselves in a state of trying to make sense of it all. They lack the knowledge they need concerning the divorce process. Both men and women are typically scared of the unknown and financial loss. Due to the emotional stress they hire an attorney quickly that may not be suitable to their personality and/or situation.

Both men and women need an unbiased and informed partner that can guide them in the right direction. Time is their most precious commodity; making costly mistakes might ruin their financial situation, enhance their stress levels and prolong the divorce process. Both parties are looking for the right answers, the right professional divorce team, i.e. lawyer, mediator, financial planner, etc. to help them get their lives back in order.

Demographics
• Men and Women
• Ages 36 to 55
• Income: 80K+ per person or $150K+ combined
• Working Professionals: dentist, managers, creative directors, bankers, etc.

Industry/Entity Type

It Company

Requirements
Must have
• Visual Feeling
• The look and feel should represent a feeling of trust and reliability.
• Use colors from the logo.
• Please select images from Q-Frame Images
• Please refer to wireframes to see where images should be placed
• Calls To Action should stand out on each page.

Use the new logo Harbor of Separation Logo and tagline: Answers, Referrals, Support.

Please use the following URL: www.harborofseparation-example.com

```html
<!DOCTYPE html>
<html lang="en">
<head>
<meta charset="utf-8">
<title>Harbor of Separation</title>
<link rel="stylesheet" href="https://fonts.googleapis.com/css2?family=Open+Sans:wght@400;600;700&family=Roboto+Condensed:wght@400;700&family=Arimo:wght@400;700&display=swap">
<style>
:root{
  --ink:#2b2b2b;
  --header:#1f1f1f;
  --footer:#262626;
  --green:#6a9a2a;
  --green-light:#8cbf3f;
  --blue:#4a86cf;
  --blue-btn:#3f7fd0;
  --form-bg:#e3e3e3;
  --field-bg:#ffffff;
  --muted:#666;
  --white:#fff;
}
*{box-sizing:border-box;margin:0;padding:0}
html,body{width:936px;height:1200px;overflow:hidden;background:#fff}
body{position:relative;font-family:"Arimo",Arial,sans-serif;color:var(--ink)}
.abs{position:absolute}

/* header */
.site-header{left:0;top:0;width:936px;height:66px;background:var(--header)}
.brand{left:140px;top:14px;display:flex;align-items:center;gap:8px}
.brand-mark{width:30px;height:30px;background:var(--green)}
.brand-name{font-family:"Open Sans",sans-serif;font-weight:700;font-size:15px;color:var(--green-light)}
.call{right:132px;top:10px;font-family:"Open Sans",sans-serif;font-size:17px;color:var(--white)}
.call span{color:var(--green-light);margin-right:6px}
.main-nav{right:132px;top:44px;display:flex;gap:26px;font-family:"Open Sans",sans-serif;font-size:10px;font-weight:600;color:var(--white);text-transform:uppercase}
.main-nav .active{color:#7fb0e8}

/* hero */
.hero{left:0;top:66px;width:936px;height:302px;background:linear-gradient(90deg,#1e2b45 0%,#3a4660 20%,#c9bfb8 55%,#e9e3df 100%)}
.hero-panel{left:123px;top:66px;width:225px;height:302px;background:var(--blue)}
.hero-title{left:142px;top:112px;font-family:"Roboto Condensed",sans-serif;font-weight:700;font-size:38px;line-height:45px;color:var(--white);text-transform:uppercase}
.hero-title .thin{font-weight:400;color:transparent;-webkit-text-stroke:1px #fff}
.video{left:360px;top:91px;width:437px;height:260px;background:#111;padding:6px}
.video-frame{width:100%;height:100%;background:radial-gradient(ellipse at 55% 45%,#c79a82 0%,#6d5a4c 40%,#2a3a2a 100%)}
.play{left:552px;top:198px}
.video-caption{right:160px;top:298px;width:180px;text-align:right;font-family:"Arimo",sans-serif;font-weight:700;color:#eee;font-size:14px;line-height:15px;white-space:nowrap}
.video-caption small{display:block;font-size:10.5px;font-weight:400;line-height:13px}

/* persona tiles */
.tile{width:186px;height:142px}
.tile-label{position:absolute;left:0;bottom:0;width:100%;height:26px;background:rgba(0,0,0,.65);color:var(--green-light);font-family:"Open Sans",sans-serif;font-size:12px;font-weight:600;line-height:26px;padding-left:12px}
.tile-plus{position:absolute;right:0;bottom:0;width:26px;height:26px;background:var(--blue);color:#fff;font-size:18px;font-weight:700;text-align:center;line-height:26px}
.t1{left:123px;top:389px;background:linear-gradient(135deg,#b3201e,#5a1210)}
.t2{left:321px;top:389px;background:linear-gradient(135deg,#6b4a2a,#c8b59a)}
.t3{left:123px;top:544px;background:linear-gradient(135deg,#e6e1d6,#6a3a1e)}
.t4{left:321px;top:544px;background:linear-gradient(135deg,#d9d9d9,#8a8a8a)}

/* lead form */
.lead-form{left:519px;top:356px;width:292px;height:333px;background:var(--form-bg)}
.form-tab{left:519px;top:356px;width:292px;height:26px;background:var(--green);color:#fff;font-family:"Roboto Condensed",sans-serif;font-weight:700;font-size:15px;line-height:26px;padding-left:10px}
.form-intro{left:537px;top:392px;width:262px;font-size:9px;line-height:12px;color:#444}
.field{width:126px;height:20px;background:var(--field-bg);border:1px solid #ccc;font-size:8.5px;line-height:12px;color:#777;padding:3px 5px;white-space:nowrap;overflow:hidden}
.field.select{padding-right:13px;font-size:8px;letter-spacing:-.15px}
.field.select::after{content:"";position:absolute;right:4px;top:8px;border:3.5px solid transparent;border-top-color:#777}
.field-area{left:534px;top:548px;width:262px;height:53px;background:#fff;border:1px solid #ccc;font-size:9px;color:#777;padding:5px 6px}
.form-note{left:533px;top:610px;width:265px;font-size:7.5px;line-height:9.5px;color:#333}
.btn-request{left:590px;top:647px;width:150px;height:27px;background:var(--blue-btn);border:1px solid #2e66ad;border-radius:3px;color:#fff;font-size:11px;font-weight:700;text-align:center;line-height:25px}

/* body copy */
.intro-copy{left:129px;top:707px;width:676px;font-size:8.3px;line-height:10px;color:#333}
.intro-copy p{margin-bottom:9px}

/* clients */
.clients{left:129px;top:897px;width:677px;height:74px;border:1px solid #d8d8d8}
.clients-title{left:153px;top:888px;background:#fff;padding:0 8px;font-family:"Open Sans",sans-serif;font-size:14px;color:#222}
.client-row{left:140px;top:918px;width:656px;display:flex;justify-content:space-between;align-items:center;height:40px}
.client{font-family:"Arimo",sans-serif;font-weight:700;font-size:13px;color:#333}
.client.c1{color:#1f5aa6}.client.c3{color:#d4262a}.client.c5{color:#e8702a}.client.c6{color:#555}
.client.c4{background:#111;color:#fff;font-size:9px;padding:5px 8px}

/* footer */
.site-footer{left:0;top:994px;width:936px;height:206px;background:var(--footer)}
.f-head{font-family:"Open Sans",sans-serif;font-size:12px;color:var(--green-light)}
.quick-links{left:145px;top:1030px;font-size:9px;line-height:17px;color:#ddd;list-style:none}
.testimonial{left:250px;top:1031px;width:156px;height:145px;border:1px solid #6a9a2a;padding:10px;color:#ddd;font-size:8.5px;line-height:11px}
.testimonial h4{font-size:9px;margin-bottom:8px}
.btn-next{left:340px;top:1152px;width:50px;height:20px;background:var(--blue-btn);border-radius:3px;color:#fff;font-size:10px;font-weight:700;text-align:center;line-height:20px}
.contact-block{left:472px;top:1055px;color:#ddd;font-size:8.5px;line-height:11px}
.corner{width:14px;height:14px;border-color:var(--green);border-style:solid}
.newsletter-field{width:156px;height:18px;background:#3a3a3a;color:#ccc;font-size:8px;padding:4px 6px}
.btn-signup{left:726px;top:1094px;width:68px;height:20px;background:#cdd8c0;color:#2d4a14;font-size:11px;font-weight:700;text-align:center;line-height:20px}
.follow{left:640px;top:1140px;font-family:"Open Sans",sans-serif;font-size:13px;color:var(--green-light)}
.social{width:22px;height:22px;background:#3b64a8}
</style>
</head>
<body>

<header class="site-header abs"></header>
<div class="brand abs"><span class="brand-mark"></span><span class="brand-name">Harbor of Separation</span></div>
<div class="call abs"><span>CALL</span>555.010.2244</div>
<nav class="main-nav abs">
  <span class="active">About Us</span><span>Services</span><span>Resources</span><span>Take Control</span><span>Contact Us</span>
</nav>

<section class="hero abs" role="img" aria-label="Photo of a man in a suit, softly blurred"></section>
<div class="hero-panel abs"></div>
<h1 class="hero-title abs"><span class="thin">If the</span><br>Solution<br><span class="thin">Is</span> Divorce,<br>Turn to us</h1>
<div class="video abs"><div class="video-frame" role="img" aria-label="Video still of the founder speaking in an office"></div></div>
<svg class="play abs" width="54" height="38" viewBox="0 0 54 38"><rect width="54" height="38" rx="9" fill="#111" opacity=".85"/><path d="M21 11 L36 19 L21 27Z" fill="#fff"/></svg>
<div class="video-caption abs">Martin Reyes<small>Founder Harbor of Separation</small></div>

<div class="tile t1 abs" role="img" aria-label="Photo of an upset couple"><span class="tile-label">Thinking of Divorce?</span><span class="tile-plus">+</span></div>
<div class="tile t2 abs" role="img" aria-label="Photo of a couple meeting a lawyer"><span class="tile-label">Need to Do Something</span><span class="tile-plus">+</span></div>
<div class="tile t3 abs" role="img" aria-label="Photo of a divorce decree with a gavel"><span class="tile-label">Recently Divorced?</span><span class="tile-plus">+</span></div>
<div class="tile t4 abs" role="img" aria-label="Photo of a pen and calculator"><span class="tile-label">Financial Help</span><span class="tile-plus">+</span></div>

<section class="lead-form abs"></section>
<div class="form-tab abs">Start Now with a Free half-hour consultation!</div>
<p class="form-intro abs">Complete this form and a Transition Specialist will answer you questions and provide direction in terms of <b>“next steps”</b>.</p>
<div class="field abs" style="left:534px;top:420px">First Name</div>
<div class="field abs" style="left:670px;top:420px">Email</div>
<div class="field select abs" style="left:534px;top:446px">Phone/Call</div>
<div class="field select abs" style="left:670px;top:446px">Best Time to Call</div>
<div class="field select abs" style="left:534px;top:471px">Annual Gross Salary</div>
<div class="field select abs" style="left:670px;top:471px">Profession</div>
<div class="field abs" style="left:534px;top:496px">Est. Net Worth</div>
<div class="field select abs" style="left:670px;top:496px">Own a primary residence</div>
<div class="field select abs" style="left:534px;top:522px">Number of children under 18?</div>
<div class="field select abs" style="left:670px;top:522px">Type of school Attended</div>
<div class="field-area abs">Question Issues you would like to discuss, If any</div>
<p class="form-note abs">All Information and details of the consultation will be held in STRICT Confidence and will not the share with outside organization or individuals (See our Policy).</p>
<div class="btn-request abs">Request More Information</div>

<section class="intro-copy abs">
  <p>Lorem Ipsum is simply dummy text of the printing and typesetting industry. Lorem Ipsum has been the industry's standard dummy text ever since the 1500s, when an unknown printer took a galley of type and scrambled it to make a type specimen book. It has survived not only five centuries, but also the leap into electronic typesetting, remaining essentially unchanged.</p>
  <p>It is a long established fact that a reader will be distracted by the readable content of a page when looking at its layout. The point of using Lorem Ipsum is that it has a more-or-less normal distribution of letters, as opposed to using 'Content here, content here', making it look like readable English. Many desktop publishing packages and web page editors now use Lorem Ipsum as their default model text, and a search for 'lorem ipsum' will uncover many web sites still in their infancy.</p>
  <p>Contrary to popular belief, Lorem Ipsum is not simply random text. It has roots in a piece of classical Latin literature from 45 BC, making it over 2000 years old. A Latin professor looked up one of the more obscure Latin words, consectetur, from a Lorem Ipsum passage, and going through the cites of the word in classical literature, discovered the undoubtable source. Lorem Ipsum comes from sections 1.10.32 and 1.10.33 of "de Finibus Bonorum et Malorum" (The Extremes of Good and Evil) by Cicero, written in 45 BC.</p>
  <p>There are many variations of passages of Lorem Ipsum available, but the majority have suffered alteration in some form, by injected humour, or randomised words which don't look even slightly believable. If you are going to use a passage of Lorem Ipsum, you need to be sure there isn't anything embarrassing hidden in the middle of text. All the Lorem Ipsum generators on the Internet tend to repeat predefined chunks as necessary, making this the first true generator on the Internet.</p>
</section>

<section class="clients abs"></section>
<h2 class="clients-title abs">Our Clients</h2>
<div class="client-row abs">
  <span class="client c1">Riverbend Water</span>
  <span class="client c2">Carter Hall</span>
  <span class="client c3">Lumen Cinemas</span>
  <span class="client c4">Eastgate Institute</span>
  <span class="client c5">Forgewell</span>
  <span class="client c6">Nodera</span>
</div>

<footer class="site-footer abs"></footer>
<h3 class="f-head abs" style="left:145px;top:1008px">Quick Links</h3>
<ul class="quick-links abs"><li>About Us</li><li>Services</li><li>Testimonials</li><li>Resources</li><li>Take Control</li><li>Contact Us</li><li>Privacy Policy</li><li>Terms</li><li>Disclamers</li></ul>
<h3 class="f-head abs" style="left:262px;top:1008px">What Peopleare Saying</h3>
<div class="testimonial abs"><h4>Testimonials</h4>Lorem Ipsum is simply dummy text of the printing and typesetting industry. Lorem Ipsum has been the industry's standard dummy text ever since the 1500s, when an unknown printer took a galley of type and scrambled it to make a type specimen book.</div>
<div class="btn-next abs">Next</div>
<div class="corner abs" style="left:446px;top:1012px;border-width:2px 0 0 2px"></div>
<div class="corner abs" style="left:606px;top:1012px;border-width:2px 2px 0 0"></div>
<div class="corner abs" style="left:446px;top:1174px;border-width:0 0 2px 2px"></div>
<div class="corner abs" style="left:606px;top:1174px;border-width:0 2px 2px 0"></div>
<h3 class="f-head abs" style="left:492px;top:1008px">Get In Touch</h3>
<div class="contact-block abs"><b>Copyright 2013</b><br><br>Harbor of Separation<br>4410 Harbor Lane Suite 12<br>Bayview, Florida 00000<br><br>555.010.2244</div>
<h3 class="f-head abs" style="left:654px;top:1008px;text-align:center;line-height:16px">Harbor of Separation Newsletter<br>Educate Yourself!</h3>
<div class="newsletter-field abs" style="left:636px;top:1048px">First Name</div>
<div class="newsletter-field abs" style="left:636px;top:1072px">Email</div>
<div class="btn-signup abs">Sign Up</div>
<div class="follow abs">Follow us</div>
<div class="social abs" style="left:703px;top:1140px" aria-label="Pagebook"></div>
<div class="social abs" style="left:730px;top:1140px;background:#2a7fb8" aria-label="Netlink"></div>

</body>
</html>
```